Stylish business cards for KX7

To create an appealing and professional business card design for a WOMEN Owned Construction Supply Company.
2 sided card. Incorporate brand elements, curvy, colorful, sleek and bright. No solid white background. attached samples of styles added shapes/ribbons. Want something with that WOW that looks awesome, factor. It is a new logo, so feel free to mess with logo colors in the blue and teal factors that can look good with both dark and light background. If you want to try a watermark with just the KX7, without the "Supply" that might look cool to.

Industry/Entity Type

Women owned construction supply company

Contact Information for Business Card

Name, Title, and phone number and email, web page. maybe spot for qr code.

Font styles to use
Sans Serif

Requirements
Nice to have
• would love to see colors, maybe stylish ribbon dividers or some sort of 2 or 3 tone color card that compliments logo.
Should not have
• Please do not have all white background. Do not include Home/reale state/ or building images.

```html
<!DOCTYPE html>
<html lang="en">
<head>
<meta charset="UTF-8">
<title>KX7 Supply – Business Cards</title>
<link href="https://fonts.googleapis.com/css2?family=Montserrat:wght@400;500;700&display=swap" rel="stylesheet">
<style>
  :root {
    --backdrop: #d3d8d8;
    --card-top: #eef3f6;
    --card-bottom: #dbe9f1;
    --navy: #1b3a63;
    --sky: #2a9bd0;
    --teal: #3cc1c9;
    --ink: #2b2d30;
  }
  * { box-sizing: border-box; margin: 0; padding: 0; }
  html, body {
    width: 1200px; height: 881px; overflow: hidden;
    background: var(--backdrop);
    font-family: "Montserrat", sans-serif;
  }
  .sheet {
    position: relative; width: 1200px; height: 881px;
    display: flex; align-items: center; justify-content: center; gap: 48px;
  }
  .card {
    width: 530px; height: 303px;
    background: linear-gradient(160deg, var(--card-top) 0%, var(--card-bottom) 100%);
    border-radius: 4px;
    box-shadow: 0 10px 24px rgba(0,0,0,0.14);
    position: relative;
    overflow: hidden;
  }
  .ribbon {
    position: absolute; left: 0; bottom: 0;
    width: 100%; height: 70px;
  }
  .card__body { position: relative; z-index: 1; height: 100%; }
  /* front */
  .card--front .card__body { display: flex; align-items: center; padding: 0 34px 30px; }
  .brand { display: flex; align-items: center; gap: 10px; color: var(--navy); font-weight: 700; white-space: nowrap; }
  .brand__dot { width: 14px; height: 14px; border-radius: 50%; background: var(--sky); flex: none; }
  .card--front .brand { width: 214px; font-size: 28px; justify-content: center; }
  .divider { width: 2px; height: 176px; background: var(--sky); margin: 0 24px 0 10px; }
  .contact { color: var(--ink); font-size: 13px; line-height: 1.55; }
  .contact__name { font-size: 20px; font-weight: 700; letter-spacing: 0.5px; color: var(--navy); line-height: 1.1; }
  .contact__name span { color: var(--sky); }
  .contact__title { margin-bottom: 10px; }
  .contact__address { margin-bottom: 8px; }
  .contact__row { display: flex; align-items: center; gap: 8px; }
  .contact__row svg { width: 12px; height: 12px; flex: none; }
  /* back */
  .card--back .card__body { display: flex; align-items: center; justify-content: center; padding-bottom: 30px; }
  .card--back .brand { font-size: 44px; gap: 14px; }
  .card--back .brand__dot { width: 20px; height: 20px; }
</style>
</head>
<body>
<main class="sheet">
  <section class="card card--front">
    <svg class="ribbon" viewBox="0 0 530 70" preserveAspectRatio="none" aria-hidden="true">
      <path d="M0 40 C140 10 300 70 530 22 L530 70 L0 70 Z" fill="#3cc1c9" opacity="0.55"/>
      <path d="M0 52 C160 28 320 76 530 38 L530 70 L0 70 Z" fill="#2a9bd0"/>
      <path d="M0 62 C180 48 340 78 530 56 L530 70 L0 70 Z" fill="#1b3a63"/>
    </svg>
    <div class="card__body">
      <div class="brand"><span class="brand__dot"></span>KX7 Supply</div>
      <div class="divider"></div>
      <div class="contact">
        <p class="contact__name">DANA <span>WHITFIELD</span></p>
        <p class="contact__title">Managing Director</p>
        <p class="contact__address">Your address, City<br>State, Zip 1234</p>
        <p class="contact__row">
          <svg viewBox="0 0 24 24" aria-hidden="true"><path fill="#2a9bd0" d="M6.6 10.8a15 15 0 0 0 6.6 6.6l2.2-2.2a1 1 0 0 1 1-.25 11.4 11.4 0 0 0 3.6.57 1 1 0 0 1 1 1V20a1 1 0 0 1-1 1A17 17 0 0 1 3 4a1 1 0 0 1 1-1h3.5a1 1 0 0 1 1 1c0 1.25.2 2.45.57 3.57a1 1 0 0 1-.25 1z"/></svg>
          123 456 789
        </p>
        <p class="contact__row">
          <svg viewBox="0 0 24 24" aria-hidden="true"><path d="M2 5h20v14H2z M2 5l10 8 10-8" fill="none" stroke="#2a9bd0" stroke-width="2.4"/></svg>
          info@kx7supply.com
        </p>
        <p class="contact__row">
          <svg viewBox="0 0 24 24" aria-hidden="true"><circle cx="12" cy="12" r="10" fill="none" stroke="#2a9bd0" stroke-width="2.4"/><path d="M2 12h20M12 2c3 3 3 17 0 20M12 2c-3 3-3 17 0 20" fill="none" stroke="#2a9bd0" stroke-width="2"/></svg>
          www.kx7supply.com
        </p>
      </div>
    </div>
  </section>
  <section class="card card--back">
    <svg class="ribbon" viewBox="0 0 530 70" preserveAspectRatio="none" aria-hidden="true">
      <path d="M0 22 C230 70 390 10 530 40 L530 70 L0 70 Z" fill="#3cc1c9" opacity="0.55"/>
      <path d="M0 38 C210 76 370 28 530 52 L530 70 L0 70 Z" fill="#2a9bd0"/>
      <path d="M0 56 C190 78 350 48 530 62 L530 70 L0 70 Z" fill="#1b3a63"/>
    </svg>
    <div class="card__body">
      <div class="brand"><span class="brand__dot"></span>KX7 Supply</div>
    </div>
  </section>
</main>
</body>
</html>
```